Dr. Martin Okelbrand
Chiropractic Physician
Simple
4817 Harwood Lane Suite B2
Miami Beach, Fl. 33127
(877) TU-VELAN (888-3526)
DrO@DrOkelbrand.example
www.DrOkelbrand.example
Im on PV, Plonkr, Wovel Net... So if someone has an Idea to throw something like that on there im up to check that out, THANKS! ALSO... I have another Toll Free number, (844)BRASK-OP. If someone wants to try it with that one in place of the TUVELAN number I would like to see which flows better on the card.
only the Okelbrand logo that is attached i want to be large and on the back of the card

```html
<!DOCTYPE html>
<html lang="en">
<head>
<meta charset="utf-8">
<title>Dr. Martin Okelbrand – Business Card</title>
<link rel="stylesheet" href="https://fonts.googleapis.com/css2?family=Open+Sans:wght@400;600&display=swap">
<style>
  :root {
    --frame-dark: #8e8e8e;
    --frame-light: #e4e4e4;
    --red: #d10f1c;
    --red-deep: #8e0710;
    --red-bright: #e3202b;
    --white: #ffffff;
    --ink: #3a3a3a;
  }
  * { box-sizing: border-box; margin: 0; padding: 0; }
  html, body { width: 1200px; height: 437px; overflow: hidden; }
  body {
    font-family: "Open Sans", Arial, sans-serif;
    background: var(--frame-dark);
    position: relative;
  }
  .backdrop-band {
    position: absolute; left: 0; top: 29px; width: 1200px; height: 367px;
    background: var(--frame-light);
  }
  .card { position: absolute; top: 53px; height: 336px; overflow: hidden; }
  .card-front { left: 43px; width: 530px; background: var(--white); }
  .card-back {
    left: 597px; width: 576px;
    background: radial-gradient(ellipse at 50% 50%, var(--red-bright) 0%, var(--red) 45%, var(--red-deep) 100%);
  }
  .front-shapes { position: absolute; inset: 0; }
  .holder-name {
    position: absolute; left: 28px; top: 97px;
    color: var(--white); font-size: 17px; font-weight: 400;
  }
  .contact {
    position: absolute; right: 18px; top: 20px;
    color: var(--white); font-size: 12px; line-height: 15px; text-align: right;
    list-style: none;
  }
  .brand {
    position: absolute; display: flex; align-items: center;
    font-weight: 400; line-height: 1;
  }
  .brand-mark { border-radius: 50%; display: block; flex: none; }
  .brand-front { left: 26px; top: 240px; color: var(--ink); font-size: 38px; gap: 10px; }
  .brand-front .brand-mark { width: 22px; height: 22px; background: var(--red); }
  .brand-back { left: 50%; top: 140px; transform: translateX(-50%); color: var(--white); font-size: 52px; gap: 12px; }
  .brand-back .brand-mark { width: 28px; height: 28px; background: var(--white); }
  .site { position: absolute; font-size: 11px; font-weight: 600; white-space: nowrap; }
  .site-front { left: 26px; top: 295px; color: var(--ink); }
  .site-back { left: 50%; top: 212px; transform: translateX(-50%); color: var(--white); font-size: 13px; }
</style>
</head>
<body>
  <div class="backdrop-band"></div>

  <section class="card card-front">
    <svg class="front-shapes" width="530" height="336" viewBox="0 0 530 336">
      <defs>
        <linearGradient id="frontRed" x1="0" y1="0" x2="1" y2="1">
          <stop offset="0" stop-color="#9a0912"/>
          <stop offset="0.5" stop-color="#d10f1c"/>
          <stop offset="1" stop-color="#e3202b"/>
        </linearGradient>
        <linearGradient id="dotFill" x1="0" y1="0" x2="1" y2="0">
          <stop offset="0" stop-color="#ffffff"/>
          <stop offset="0.6" stop-color="#ecdcdc"/>
          <stop offset="1" stop-color="#f4eaea"/>
        </linearGradient>
      </defs>
      <path d="M0 0 H530 V140 C420 150 350 205 245 190 C150 175 80 150 0 180 Z" fill="url(#frontRed)"/>
      <path role="img" aria-label="Soft dotted pattern area" d="M0 205 C80 175 150 198 245 212 C350 228 420 172 530 160 V336 H0 Z" fill="url(#dotFill)" opacity="0.8"/>
    </svg>
    <h1 class="holder-name">Dr. Martin Okelbrand</h1>
    <ul class="contact">
      <li>4817 Harwood Lane Suite B2</li>
      <li>Miami Beach, Fl. 33127</li>
      <li>Toll free: (877) TU-VELAN (888-3526)</li>
      <li>Email: DrO@DrOkelbrand.example</li>
      <li>www.DrOkelbrand.example</li>
    </ul>
    <div class="brand brand-front"><span>Okelbrand</span><span class="brand-mark"></span></div>
    <p class="site site-front">www.DrOkelbrand.example</p>
  </section>

  <section class="card card-back">
    <div class="brand brand-back"><span>Okelbrand</span><span class="brand-mark"></span></div>
    <p class="site site-back">www.DrOkelbrand.example</p>
  </section>
</body>
</html>
```